Webdesign für Onlineshop
Zielgruppe
Wir verkaufen in unserem Onlineshop alles zum Thema Wohnen mit dem Schwerpunkt Möbel. Die Hauptzielgruppe ist zwischen 25 und 45 Jahren.
Aufgabenstellung
Wir bevorzugen ein modernes, flaches und aufgeräumtes Design ähnlich wie velm.de / dorano88.de mit dem Fokus auf Preisaggressivität und Rabatte.
- Das Grundlayout muss so bleiben, wie es aktuell ist. Natürlich dürfen einzelne Elemente verschoben / versetzt werden.
- Im Header sollte Platz für eine kleine Werbefläche sein (ähnlich wie der konfigurierbare Kleiderschrank).
- Der Shop basiert auf Magento 1.9.
- Die Rabatte in den Produktdetailseiten müssen genauso aufgebaut sein
- Die Suche sollte in den Header platziert werden und nicht im Menü
- Ein SSL Logo soll im Header platziert weden
- Die Vorteile (Kostenloser Versand, Sicher einkaufen, Kauf auf Rechnung) sollen im Header erscheinen
- Das Design sollte responsive sein
Es wird nur das reine Design ohne Programmierung benötigt.

```html
<!DOCTYPE html>
<html lang="de">
<head>
<meta charset="utf-8">
<title>quellmark3berg – Onlineshop</title>
<link rel="stylesheet" href="https://fonts.googleapis.com/css2?family=Open+Sans:wght@300;400;600&family=Roboto:wght@300;400;500;700&display=swap">
<style>
:root{
  --green:#76a73a;
  --blue:#3ea3c0;
  --text:#333;
  --muted:#666;
  --line:#e4e4e4;
  --topbar:#f6f6f6;
  --white:#fff;
}
*{box-sizing:border-box;margin:0;padding:0}
html,body{width:784px;height:1200px;overflow:hidden;background:var(--white)}
body{position:relative;font-family:"Open Sans",sans-serif;color:var(--text)}
.abs{position:absolute}
.topbar{left:0;top:0;width:784px;height:24px;background:var(--topbar)}
.phone{left:111px;top:4px;font:500 13px/16px "Roboto",sans-serif;color:#555;display:flex;align-items:center;gap:4px}
.hours{font-size:4px;line-height:5px;color:#555;margin-left:4px;font-family:"Open Sans",sans-serif}
.promo-badge{left:316px;top:0;width:27px;height:27px;border-radius:50%;background:var(--blue);color:#fff;font:700 12px/27px "Roboto",sans-serif;text-align:center;letter-spacing:-.5px}
.promo-text{left:347px;top:2px}
.promo-title{font:500 10px/12px "Roboto",sans-serif;color:var(--blue)}
.promo-sub{font-size:5px;line-height:7px;color:#555}
.voucher{left:550px;top:8px;font-size:6px;color:#444}
.contact{left:652px;top:8px;font-size:6px;color:#444}
.topsep{left:641px;top:6px;width:1px;height:12px;background:var(--line)}
.logo{left:110px;top:40px;font:700 21px/26px "Roboto",sans-serif;color:var(--green);letter-spacing:-.5px}
.search{left:263px;top:43px;width:297px;height:25px;border:1px solid var(--line);border-radius:2px;font-size:9px;line-height:23px;padding-left:10px;color:#666}
.search svg{position:absolute;right:9px;top:6px}
.seal{top:42px;width:26px;height:26px;border-radius:50%;background:#9a9a9a;border:2px solid #d2d2d2}
.seal.square{border-radius:3px;width:18px;background:#bbb}
.nav{left:0;top:90px;width:784px;height:38px;border-top:1px solid var(--line)}
.nav a{position:absolute;top:0;height:38px;line-height:38px;font:400 7.5px/38px "Roboto",sans-serif;color:#222;text-decoration:none;letter-spacing:.2px}
.nav a.active{background:var(--green);color:#fff;padding:0 7px}
.nav a.sale{color:var(--blue);font-weight:700}
.nav .divider{position:absolute;top:0;width:1px;height:38px;background:var(--line)}
.cart-count{left:661px;top:94px;width:16px;height:16px;border-radius:50%;background:var(--blue);color:#fff;font:700 9px/16px "Roboto",sans-serif;text-align:center}
.hero{left:0;top:128px;width:784px;height:296px;background:linear-gradient(90deg,#cfcdca 0%,#a69d93 45%,#8d8379 60%,#bdb5ab 100%)}
.hero-title{left:0;top:172px;width:784px;text-align:center;font:500 24px/31px "Roboto",sans-serif;color:#fff;text-shadow:0 1px 3px rgba(0,0,0,.4)}
.btn{font:500 9.5px/1 "Roboto",sans-serif;color:#fff;text-align:center;letter-spacing:.3px;display:flex;align-items:center;justify-content:center;border-radius:2px}
.btn.blue{background:var(--blue)}
.btn.green{background:var(--green)}
.hero-btn{left:333px;top:336px;width:112px;height:36px;font-size:11px}
.hero-arrow{top:261px;width:30px;height:30px;border-radius:50%;background:#fff;display:flex;align-items:center;justify-content:center}
.dot{top:391px;width:7px;height:7px;border-radius:50%;border:1px solid #fff}
.dot.on{background:var(--blue);border-color:var(--blue)}
.benefit-icon{top:443px;width:40px;height:40px;border-radius:50%;border:1px solid #ddd;display:flex;align-items:center;justify-content:center}
.benefit-text{top:454px;font-size:10px;line-height:14px;color:#333}
.benefit-sep{top:444px;width:1px;height:34px;background:#eee}
.tile{top:500px;width:277px;height:192px}
.tile-title{font:700 16.5px/20px "Roboto",sans-serif;color:#fff;text-shadow:0 1px 3px rgba(0,0,0,.6)}
.tile-btn{width:108px;height:32px}
.section-title{left:109px;top:720px;font:300 16px/20px "Roboto",sans-serif;color:#222;letter-spacing:.2px}
.round-arrow{top:717px;width:30px;height:30px;border-radius:50%;border:1px solid #ddd;display:flex;align-items:center;justify-content:center}
.product-img{top:760px;width:134px;height:91px}
.discount{top:755px;width:34px;height:34px;border-radius:50%;background:var(--blue);color:#fff;font:500 10px/34px "Roboto",sans-serif;text-align:center}
.product-name{top:862px;width:120px;font-size:8.5px;line-height:11px;color:#444}
.old-price{top:891px;font-size:7.5px;color:#444;text-decoration:line-through}
.price{top:902px;font:400 13px/16px "Roboto",sans-serif;color:var(--blue)}
.kids{left:110px;top:958px;width:563px;height:222px;border:1px solid var(--line);overflow:hidden}
.kids-img{position:absolute;right:0;top:0;width:430px;height:222px;background:linear-gradient(90deg,rgba(255,255,255,1) 0%,rgba(233,238,226,.9) 30%,#e6d7c6 55%,#d9e4ea 80%,#a9cfe3 100%)}
.kids-title{left:145px;top:980px;font:300 21px/26px "Open Sans",sans-serif;color:#222}
.kids-text{left:146px;top:1011px;width:230px;font:300 9.5px/13.5px "Open Sans",sans-serif;color:#333}
.kids-price{left:147px;top:1058px;font:400 23px/28px "Roboto",sans-serif;color:var(--blue)}
.kids-btn{left:147px;top:1114px;width:108px;height:32px}
</style>
</head>
<body>

<div class="abs topbar"></div>
<div class="abs phone">
  <svg width="12" height="12" viewBox="0 0 12 12"><circle cx="6" cy="6" r="5.3" fill="none" stroke="#76a73a" stroke-width="1"/><path d="M4 3.3l1 1.3-.6.7c.4.9 1 1.5 1.9 1.9l.7-.6 1.3 1-.6 1c-2.4-.3-4.1-2-4.4-4.4z" fill="#76a73a"/></svg>
  0571 / 47 26 13 90
  <span class="hours">Mo-Fr 9-21 Uhr<br>Sa 10-15 Uhr</span>
</div>
<div class="abs promo-badge">10%</div>
<div class="abs promo-text">
  <div class="promo-title">EINFÜHRUNGSRABATTE ›</div>
  <div class="promo-sub">Kleiderschrank jetzt auch selbst zusammenstellen</div>
</div>
<div class="abs voucher">5 € Gutschein jetzt sichern! ⌄</div>
<div class="abs topsep"></div>
<div class="abs contact">Kontakt</div>

<div class="abs logo">quellmark3berg</div>
<div class="abs search">Suche...
  <svg width="11" height="11" viewBox="0 0 11 11"><circle cx="4.5" cy="4.5" r="3.6" fill="none" stroke="#777" stroke-width="1"/><path d="M7.2 7.2l3 3" stroke="#777" stroke-width="1"/></svg>
</div>
<div class="abs seal" style="left:579px"></div>
<div class="abs seal" style="left:618px"></div>
<div class="abs seal square" style="left:657px;top:43px"></div>

<nav class="abs nav">
  <a style="left:111px">WOHNEN</a>
  <a class="active" style="left:154px">SCHLAFEN</a>
  <a style="left:217px">KINDER-BABY</a>
  <a style="left:282px">ESSEN</a>
  <a style="left:323px">KUCHE</a>
  <a style="left:364px">BIS 60% RABATT</a>
  <a style="left:440px">SONSTIGES</a>
  <a class="sale" style="left:498px">SALE</a>
  <span class="divider" style="left:103px"></span>
  <span class="divider" style="left:540px"></span>
  <span class="divider" style="left:587px"></span>
  <span class="divider" style="left:634px"></span>
  <span class="divider" style="left:681px"></span>
  <svg style="position:absolute;left:555px;top:10px" width="17" height="18" viewBox="0 0 17 18"><circle cx="8.5" cy="6" r="4" fill="none" stroke="#333" stroke-width="1"/><path d="M1.5 17c0-4 3-6 7-6s7 2 7 6z" fill="none" stroke="#333" stroke-width="1"/></svg>
  <svg style="position:absolute;left:602px;top:11px" width="17" height="17" viewBox="0 0 17 17"><path d="M1 1h7l8 8-7 7-8-8z" fill="none" stroke="#333" stroke-width="1"/><circle cx="4.5" cy="4.5" r="1.2" fill="none" stroke="#333" stroke-width="1"/></svg>
  <svg style="position:absolute;left:645px;top:12px" width="22" height="17" viewBox="0 0 22 17"><path d="M1 1h3l3 10h11l2-7H6" fill="none" stroke="#333" stroke-width="1"/><circle cx="9" cy="14.5" r="1.5" fill="none" stroke="#333"/><circle cx="16" cy="14.5" r="1.5" fill="none" stroke="#333"/></svg>
</nav>
<div class="abs cart-count">3</div>

<div class="abs hero" role="img" aria-label="Helles Schlafzimmer mit Bett, Steinwand, Kleiderschrank und Kommode"></div>
<h1 class="abs hero-title">Matratzen mit Komfort für<br>mehr Schlafqualität</h1>
<div class="abs btn blue hero-btn">40% GESPART</div>
<div class="abs hero-arrow" style="left:53px"><svg width="10" height="10" viewBox="0 0 10 10"><path d="M9 5H1M4.5 1.5L1 5l3.5 3.5" fill="none" stroke="#222" stroke-width="1.3"/></svg></div>
<div class="abs hero-arrow" style="left:671px"><svg width="10" height="10" viewBox="0 0 10 10"><path d="M1 5h8M5.5 1.5L9 5 5.5 8.5" fill="none" stroke="#222" stroke-width="1.3"/></svg></div>
<span class="abs dot" style="left:367px"></span>
<span class="abs dot on" style="left:381px"></span>
<span class="abs dot" style="left:396px"></span>
<span class="abs dot" style="left:410px"></span>

<div class="abs benefit-icon" style="left:127px"><svg width="22" height="16" viewBox="0 0 22 16"><rect x="8" y="1" width="13" height="10" fill="none" stroke="#3ea3c0" stroke-width="1.2"/><path d="M8 5H4L1 8v4h7" fill="none" stroke="#3ea3c0" stroke-width="1.2"/><circle cx="5" cy="13" r="2" fill="#3ea3c0"/><circle cx="16" cy="13" r="2" fill="#3ea3c0"/></svg></div>
<div class="abs benefit-text" style="left:184px">Kostenloser Versand</div>
<div class="abs benefit-sep" style="left:301px"></div>
<div class="abs benefit-icon" style="left:326px"><svg width="16" height="20" viewBox="0 0 16 20"><rect x="1" y="6" width="14" height="13" rx="1.5" fill="none" stroke="#3ea3c0" stroke-width="1.2"/><path d="M4.5 6V4a3.5 3.5 0 0 1 7 0v2" fill="none" stroke="#3ea3c0" stroke-width="1.2"/><path d="M4.5 12.5l2.3 2.3 4.5-4.5" fill="none" stroke="#3ea3c0" stroke-width="1.4"/></svg></div>
<div class="abs benefit-text" style="left:392px">Sicher einkaufen</div>
<div class="abs benefit-sep" style="left:507px"></div>
<div class="abs benefit-icon" style="left:526px"><svg width="18" height="20" viewBox="0 0 18 20"><rect x="2" y="1" width="13" height="17" fill="none" stroke="#3ea3c0" stroke-width="1.2"/><path d="M5 6h7M5 9h7M5 12h5" stroke="#3ea3c0" stroke-width="1.2"/><rect x="2" y="16" width="15" height="3" fill="#3ea3c0"/></svg></div>
<div class="abs benefit-text" style="left:580px">Kauf auf Rechnung</div>

<div class="abs tile" style="left:110px;background:linear-gradient(90deg,#8c6f5a,#d2b16a 35%,#e7c7a9 50%,#6d88b3 75%,#c6c2bd)" role="img" aria-label="Frau vor einem gefüllten Kleiderschrank"></div>
<div class="abs tile-title" style="left:135px;top:593px">Ihr ganz persönlicher<br>Kleiderschrank</div>
<div class="abs btn green tile-btn" style="left:136px;top:642px">40% GESPART</div>
<div class="abs tile" style="left:397px;background:linear-gradient(135deg,#5b5b58,#b8b6ae 40%,#4a4a48 70%,#222)" role="img" aria-label="Schwarze Relaxsessel vor großen Loftfenstern"></div>
<div class="abs tile-title" style="left:421px;top:593px">Holen sie sich das ganz<br>grosse kino nach hause</div>
<div class="abs btn green tile-btn" style="left:422px;top:642px">40% GESPART</div>

<h2 class="abs section-title">UNSERE TOPSELLER</h2>
<div class="abs round-arrow" style="left:605px"><svg width="9" height="9" viewBox="0 0 10 10"><path d="M9 5H1M4.5 1.5L1 5l3.5 3.5" fill="none" stroke="#555" stroke-width="1.1"/></svg></div>
<div class="abs round-arrow" style="left:643px"><svg width="9" height="9" viewBox="0 0 10 10"><path d="M1 5h8M5.5 1.5L9 5 5.5 8.5" fill="none" stroke="#555" stroke-width="1.1"/></svg></div>

<div class="abs product-img" style="left:110px;background:linear-gradient(180deg,#e8e8e6,#5a5a5a 60%,#d8d8d2)" role="img" aria-label="Schwarzes Boxspringbett"></div>
<div class="abs discount" style="left:107px">-36%</div>
<div class="abs product-name" style="left:118px">Wohnlandschaft, in Mikrofaser Vintage-Look</div>
<div class="abs old-price" style="left:118px">999,00 €</div>
<div class="abs price" style="left:118px">575,10 €</div>

<div class="abs product-img" style="left:254px;background:linear-gradient(180deg,#8a7462,#d8c2a1 45%,#62c3c6 70%,#c9b48f)" role="img" aria-label="Schlafzimmer in Eiche-Dekor mit türkiser Bettwäsche"></div>
<div class="abs discount" style="left:250px">-27%</div>
<div class="abs product-name" style="left:262px">Schlafzimmerkombination 4-tlg. in Eiche-Dekor mit Abs.</div>
<div class="abs old-price" style="left:262px">999,00 €</div>
<div class="abs price" style="left:262px">575,10 €</div>

<div class="abs product-img" style="left:397px;background:linear-gradient(180deg,#8fb3bd,#e9eef0 45%,#6f6f70 70%,#e6e6e6)" role="img" aria-label="Weißer Esstisch mit grauen Stühlen"></div>
<div class="abs discount" style="left:392px">-36%</div>
<div class="abs product-name" style="left:405px">Boxspringbett schwarz, Feinstrukturstoff</div>
<div class="abs old-price" style="left:405px">999,00 €</div>
<div class="abs price" style="left:405px">575,10 €</div>

<div class="abs product-img" style="left:540px;background:linear-gradient(180deg,#dedcda,#cfcac6 45%,#6b4232 70%,#4a2a20)" role="img" aria-label="Braunes Schlafsofa vor heller Wand"></div>
<div class="abs discount" style="left:536px">-34%</div>
<div class="abs product-name" style="left:548px">Boxspringbett schwarz, Feinstrukturstoff</div>
<div class="abs old-price" style="left:548px">999,00 €</div>
<div class="abs price" style="left:548px">575,10 €</div>

<div class="abs kids"><div class="kids-img" role="img" aria-label="Lächelnde Mutter mit Tochter"></div></div>
<h2 class="abs kids-title">Kindgerecht und schön!</h2>
<p class="abs kids-text">Entdecken Sie unsere kindgerechten Baby- und Kinderzimmer und zaubern Sie ihren Kleinen ein wundervolles Lächeln ins Gesicht!</p>
<div class="abs kids-price">445,47 €</div>
<div class="abs btn green kids-btn">40% GESPART</div>

</body>
</html>
```